Request for Business Card Design

Hi. My name is Marlena, I am looking for a new business card design for my company, Quillbrook Sensing Systems, LLC. I really like the design you did for Tavel Harvest and was hoping you could do something similar using our full logo and our mark. I am also open to any raised texture design using our mark. I have attached our full logo, which would need to be somewhere on the card, as well as the mark in both outline and full form, as well as our brand colors / guide. The card does not have to be white, as long as our logo and mark appear. I actually like darker colored business cards more, but am open to all options. If you are interested in working with me, please let me know. We would also take the business card design into letterhead design if you can do that.

```html
<!DOCTYPE html>
<html lang="en">
<head>
<meta charset="utf-8">
<title>Quillbrook Sensing Systems – Business Card</title>
<link rel="stylesheet" href="https://fonts.googleapis.com/css2?family=Barlow:wght@400;500;700&display=swap">
<style>
  :root {
    --stage-dark: #141414;
    --stage-mid: #2a2a2a;
    --card-blue: #0a98c0;
    --card-blue-light: #12a9d2;
    --ink-white: #ffffff;
    --ink-soft: rgba(255,255,255,0.88);
  }
  * { box-sizing: border-box; margin: 0; padding: 0; }
  html, body { width: 1200px; height: 875px; overflow: hidden; }
  body {
    background: radial-gradient(ellipse at 40% 45%, var(--stage-mid), var(--stage-dark) 75%);
    font-family: "Barlow", sans-serif;
    color: var(--ink-white);
    position: relative;
  }
  .card {
    position: absolute;
    width: 540px;
    height: 310px;
    border-radius: 26px;
    background: linear-gradient(135deg, var(--card-blue-light), var(--card-blue) 60%);
    box-shadow: 0 24px 50px rgba(0,0,0,0.55);
    overflow: hidden;
  }
  .card-front { left: 70px; top: 130px; }
  .card-back { left: 590px; top: 430px; }

  .brand { display: flex; align-items: center; gap: 18px; }
  .brand-dot {
    width: 58px; height: 58px; border-radius: 50%;
    background: var(--ink-white); flex: none;
  }
  .brand-name {
    font-weight: 700; font-size: 46px; letter-spacing: 5px; line-height: 1;
  }
  .brand-tagline {
    font-weight: 500; font-size: 14px; letter-spacing: 1.6px; margin-top: 4px;
  }
  .card-front .brand {
    position: absolute; left: 70px; top: 50%; transform: translateY(-50%);
  }

  .card-back .brand { position: absolute; left: 40px; top: 40px; gap: 14px; }
  .card-back .brand-dot { width: 42px; height: 42px; }
  .card-back .brand-name { font-size: 32px; letter-spacing: 3.5px; }
  .card-back .brand-tagline { font-size: 10px; letter-spacing: 1.2px; }

  .holder { position: absolute; left: 40px; top: 140px; }
  .holder-name { font-weight: 700; font-size: 24px; letter-spacing: 0.5px; }
  .holder-role { font-weight: 400; font-size: 14px; letter-spacing: 1px; color: var(--ink-soft); margin-top: 2px; }

  .contacts { list-style: none; margin-top: 16px; }
  .contacts li {
    display: flex; align-items: center; gap: 10px;
    font-size: 14px; color: var(--ink-soft); line-height: 1.75;
  }
  .contacts svg { width: 14px; height: 14px; flex: none; }

  .address {
    position: absolute; right: 36px; bottom: 36px;
    text-align: right; font-size: 13px; line-height: 1.5; color: var(--ink-soft);
  }
</style>
</head>
<body>
  <section class="card card-front" aria-label="Card front">
    <div class="brand">
      <span class="brand-dot"></span>
      <div>
        <div class="brand-name">QUILLBROOK</div>
        <div class="brand-tagline">SENSING SYSTEMS</div>
      </div>
    </div>
  </section>

  <section class="card card-back" aria-label="Card back">
    <div class="brand">
      <span class="brand-dot"></span>
      <div>
        <div class="brand-name">QUILLBROOK</div>
        <div class="brand-tagline">SENSING SYSTEMS</div>
      </div>
    </div>

    <div class="holder">
      <div class="holder-name">TOBIAS RENNER</div>
      <div class="holder-role">MANAGING DIRECTOR</div>
      <ul class="contacts">
        <li>
          <svg viewBox="0 0 24 24" aria-hidden="true"><path fill="#fff" d="M6.6 10.8a15.1 15.1 0 0 0 6.6 6.6l2.2-2.2c.3-.3.7-.4 1-.2 1.1.4 2.3.6 3.6.6.6 0 1 .4 1 1V20c0 .6-.4 1-1 1A17 17 0 0 1 3 4c0-.6.4-1 1-1h3.5c.6 0 1 .4 1 1 0 1.3.2 2.5.6 3.6.1.3 0 .7-.2 1z"/></svg>
          044-555 018 274
        </li>
        <li>
          <svg viewBox="0 0 24 24" aria-hidden="true"><path fill="#fff" d="M3 5h18v14H3z"/><path fill="none" stroke="#0a98c0" stroke-width="2" d="M3 5l9 8 9-8"/></svg>
          info@quillbrooksense.com
        </li>
        <li>
          <svg viewBox="0 0 24 24" aria-hidden="true"><g fill="none" stroke="#fff" stroke-width="2"><circle cx="12" cy="12" r="9"/><path d="M3 12h18M12 3c3 3 3 15 0 18M12 3c-3 3-3 15 0 18"/></g></svg>
          www.quillbrooksense.com
        </li>
      </ul>
    </div>

    <address class="address" style="font-style: normal;">
      88, Larkspur Avenue West<br>
      30917, Norvale
    </address>
  </section>
</body>
</html>
```